Popup Nightclub Grand Opening Flyer

We need to design a flyer for the grand opening of an upscale, exclusive nightclub called "Lanternfall". The design needs to be chic and exclusive. The background should be black and the text should primarily be white. We like minimalist designs.

Here is the text for the flyer
-
Velvetrope Atlanta Presents

Lanternfall (LOGO)

A Popup Nightclub Experience
For one night Only

Friday, October 18, 2013
Party begins at 9PM

INVITE ONLY

See invitation for location details
(Velvetrope Atlanta logo)

-
Examples we like

http://cdn2-b.brivelpost.com/sites/default/files/styles/image_content_width/hash/3d/fa/1472093815_4471_flyer.jpg?itok=R8kqWm2z

http://api.plovra.com/files/7Kqq-Tr82XXB3pQzJvmtR5HL2W719E4nbRtC6KLd4HsfM8Y2qTDK-VmjwDoNqLX4QBzTHD9nakRbVx3m-Pfq8htc3MDTWr5p4/2zelSaturdays.jpg

http://quenmar.com/wp-content/uploads/yootheme/widgetkit/gallery/2zel/2zel-gen_vroom4-01.jpg

Hi All, one thing that we are seeing that we don't like is on over emphasis on the phrase "a popup nightclub experience" please don't make this the largest thing on the flyer

Target Market(s)

Target market is 25-35 year olds who are affluent (rich) and like luxury brands

Requirements
Must have
• Dark Background
Nice to have
• Velvetrope Logo on the bottom
Modern text that isn't curvy
Should not have
• Curved text

```html
<!DOCTYPE html>
<html lang="en">
<head>
<meta charset="utf-8">
<title>Lanternfall — A Pop-Up Nightclub Experience</title>
<link rel="stylesheet" href="https://fonts.googleapis.com/css2?family=Montserrat:wght@300;400&family=Oswald:wght@300;400;500&display=swap">
<style>
  :root {
    --bg-deep: #050505;
    --bg-mid: #1c1c1c;
    --ink: #f2f2f2;
    --ink-soft: #b9b9b9;
    --silver-light: #d8d8d8;
    --silver-dark: #7a7a7a;
    --rule: #8c8c8c;
  }
  * { margin: 0; padding: 0; box-sizing: border-box; }
  html, body {
    width: 849px;
    height: 1200px;
    overflow: hidden;
    background: var(--bg-deep);
  }
  .flyer {
    position: relative;
    width: 849px;
    height: 1200px;
    overflow: hidden;
    background: radial-gradient(ellipse at 50% 40%, var(--bg-mid) 0%, #101010 45%, var(--bg-deep) 100%);
    color: var(--ink);
    text-align: center;
    font-family: "Montserrat", sans-serif;
  }
  .flyer > * {
    position: absolute;
    left: 0;
    right: 0;
  }
  .presenter {
    top: 50px;
    font-size: 24px;
    font-weight: 400;
    letter-spacing: 5px;
    text-transform: uppercase;
  }
  .brand-mark {
    top: 190px;
    display: flex;
    justify-content: center;
  }
  .brand-name {
    top: 515px;
    font-size: 64px;
    font-weight: 300;
    letter-spacing: 10px;
    text-transform: uppercase;
  }
  .rule {
    left: 50%;
    height: 2px;
    background: var(--rule);
    transform: translateX(-50%);
  }
  .rule--top { top: 655px; width: 540px; }
  .rule--mid { top: 708px; width: 540px; }
  .rule--short { top: 832px; width: 140px; height: 1px; }
  .tagline {
    top: 662px;
    font-family: "Oswald", sans-serif;
    font-size: 34px;
    font-weight: 500;
    letter-spacing: 3px;
    text-transform: uppercase;
  }
  .timing {
    top: 712px;
    font-family: "Oswald", sans-serif;
    font-size: 22px;
    font-weight: 300;
    letter-spacing: 4px;
    color: var(--ink-soft);
    text-transform: uppercase;
  }
  .event-date {
    top: 740px;
    font-family: "Oswald", sans-serif;
    font-size: 60px;
    font-weight: 300;
    letter-spacing: 1px;
    text-transform: uppercase;
  }
  .access {
    top: 866px;
    font-size: 17px;
    font-weight: 400;
    letter-spacing: 4px;
    text-transform: uppercase;
  }
  .location-note {
    top: 898px;
    font-size: 13px;
    font-weight: 400;
    letter-spacing: 2px;
    color: var(--ink-soft);
    text-transform: uppercase;
  }
  .host-sign {
    top: 1142px;
    display: flex;
    justify-content: center;
    align-items: center;
    gap: 12px;
    font-size: 20px;
    font-weight: 400;
    letter-spacing: 4px;
    text-transform: uppercase;
  }
  .host-sign__square {
    width: 26px;
    height: 26px;
    background: var(--ink);
  }
</style>
</head>
<body>
  <main class="flyer">
    <p class="presenter">Velvetrope Atlanta Presents</p>

    <div class="brand-mark">
      <svg width="230" height="230" viewBox="0 0 230 230" aria-hidden="true">
        <defs>
          <linearGradient id="silver" x1="0" y1="0" x2="1" y2="1">
            <stop offset="0" stop-color="var(--silver-light)"/>
            <stop offset="1" stop-color="var(--silver-dark)"/>
          </linearGradient>
        </defs>
        <circle cx="115" cy="115" r="110" fill="url(#silver)"/>
      </svg>
    </div>

    <h1 class="brand-name">Lanternfall</h1>

    <div class="rule rule--top"></div>
    <p class="tagline">A Pop-Up Nightclub Experience</p>
    <div class="rule rule--mid"></div>
    <p class="timing">For one night only | Party begins at 9PM</p>
    <p class="event-date">Friday, October 18, 2013</p>
    <div class="rule rule--short"></div>

    <p class="access">Invite Only</p>
    <p class="location-note">See invitation for location details</p>

    <div class="host-sign">
      <span class="host-sign__square"></span>
      <span class="host-sign__name">Velvetrope</span>
    </div>
  </main>
</body>
</html>
```